Travel Blogger Business Card for roamquill.net

I need a two-sided business card for a travel blogging website. The card should be both professional and fun at the same time. This is for the website www.roamquill.net

I don't necessarily think that the current logo on the website needs to be used on the business card but it can be. I am very flexible with ideas

Target Market(s)

Travel agencies that will be met at a conference.

Industry/Entity Type

Travel

Contact Information for Business Card

Company Name: Roam Quill.net
Name: Bertrand Olesky
Voice: +1-(345)-402-7731
Address: Coral Reach Shore, Grand Cayman, Cayman Islands
Email: ceo@roamquill.net

Colors
0592cd
0355a3
3176b5
33a6d7
85cae6
85acd3

Requirements
Must have
• Website address and name should be bigger than address, phone number, and email.

```html
<!DOCTYPE html>
<html lang="en">
<head>
<meta charset="utf-8">
<title>Roam Quill – Business Card</title>
<link href="https://fonts.googleapis.com/css2?family=Open+Sans:wght@400;600;700;800&display=swap" rel="stylesheet">
<style>
  :root {
    --stage: #2b2b2d;
    --teal: #0b7c93;
    --teal-light: #33a6d7;
    --paper: #ffffff;
    --ink: #0b0b0c;
    --ink-text: #1d1d1f;
    --muted: #d9d9d9;
  }
  * { box-sizing: border-box; margin: 0; padding: 0; }
  html, body {
    width: 1200px; height: 900px; overflow: hidden;
    background: var(--stage);
    font-family: "Open Sans", Arial, sans-serif;
  }
  .sheet {
    width: 1200px; height: 900px;
    display: flex; flex-direction: column; align-items: center; justify-content: center;
    gap: 40px;
  }
  .card {
    position: relative;
    width: 700px; height: 400px;
    border-radius: 22px;
    overflow: hidden;
    background: var(--paper);
    box-shadow: 0 10px 30px rgba(0,0,0,.45);
  }
  .card-shape { position: absolute; inset: 0; }
  .brand-name {
    position: absolute;
    font-weight: 800;
    color: var(--paper);
    letter-spacing: 1px;
    text-transform: uppercase;
    display: flex; align-items: center; gap: 14px;
    white-space: nowrap;
  }
  .brand-dot {
    width: 38px; height: 38px; border-radius: 50%;
    background: var(--paper);
  }

  /* Front */
  .front .brand-main { left: 60px; top: 200px; font-size: 44px; }
  .front .brand-top { right: 36px; top: 92px; font-size: 40px; }
  .front .web {
    position: absolute; left: 26px; bottom: 16px;
    font-size: 17px; color: var(--ink-text);
  }
  .front .web strong { color: var(--teal); font-weight: 700; }

  /* Back */
  .back .brand-main { left: 44px; top: 188px; font-size: 34px; }
  .back .brand-main .brand-dot { width: 30px; height: 30px; }
  .contact {
    position: absolute; left: 410px; top: 80px;
    padding-left: 18px;
    border-left: 1px solid #777;
    color: var(--muted);
    font-size: 13px; line-height: 1.5;
  }
  .contact .person {
    color: var(--teal-light); font-weight: 700; font-size: 18px;
    text-transform: uppercase; letter-spacing: .5px; margin-bottom: 4px;
  }
  .contact .address { margin-bottom: 10px; }
  .contact ul { list-style: none; }
  .contact li { display: flex; align-items: center; gap: 10px; margin-bottom: 3px; }
  .contact li.site { font-size: 16px; color: var(--paper); }
  .contact li.site strong { font-weight: 700; }
  .icon { width: 16px; height: 16px; flex: none; }
</style>
</head>
<body>
<main class="sheet">

  <section class="card front" aria-label="Card front">
    <svg class="card-shape" viewBox="0 0 700 400" preserveAspectRatio="none" aria-hidden="true">
      <path fill="var(--teal)" d="M0 28 H380 C396 28 400 62 418 62 H700 V372 H362 C344 372 344 338 326 338 H0 Z"/>
    </svg>
    <div class="brand-name brand-top">Roam Quill</div>
    <div class="brand-name brand-main"><span class="brand-dot"></span>Roam Quill</div>
    <p class="web">www.<strong>roamquill</strong>.net</p>
  </section>

  <section class="card back" aria-label="Card back">
    <svg class="card-shape" viewBox="0 0 700 400" preserveAspectRatio="none" aria-hidden="true">
      <path fill="var(--ink)" d="M0 58 H300 C318 58 320 24 340 24 H700 V340 H600 C580 340 580 378 562 378 H0 Z"/>
    </svg>
    <div class="brand-name brand-main"><span class="brand-dot"></span>Roam Quill</div>
    <div class="contact">
      <p class="person">Bertrand Olesky</p>
      <p class="address">Coral Reach Shore<br>Grand Cayman, Cayman Islands</p>
      <ul>
        <li>
          <svg class="icon" viewBox="0 0 16 16" aria-hidden="true"><circle cx="8" cy="8" r="8" fill="var(--teal-light)"/><path d="M5 4.5l1.6-.4.9 2-1 .8a5 5 0 0 0 2.6 2.6l.8-1 2 .9-.4 1.6c-3.5.3-6.8-3-6.5-6.5z" fill="var(--ink)"/></svg>
          +1-(345)-402-7731
        </li>
        <li>
          <svg class="icon" viewBox="0 0 16 16" aria-hidden="true"><circle cx="8" cy="8" r="8" fill="var(--teal-light)"/><rect x="4" y="5" width="8" height="6" rx="1" fill="var(--ink)"/><path d="M4.5 5.5L8 8.3l3.5-2.8" stroke="var(--teal-light)" fill="none"/></svg>
          ceo@roamquill.net
        </li>
        <li class="site">
          <svg class="icon" viewBox="0 0 16 16" aria-hidden="true"><circle cx="8" cy="8" r="8" fill="var(--teal-light)"/><circle cx="8" cy="8" r="4" fill="none" stroke="var(--ink)"/><path d="M4 8h8M8 4c-2 2.5-2 5.5 0 8M8 4c2 2.5 2 5.5 0 8" fill="none" stroke="var(--ink)"/></svg>
          <span>www.<strong>roamquill</strong>.net</span>
        </li>
      </ul>
    </div>
  </section>

</main>
</body>
</html>
```